Bramblecrest Capital Partners Needs a Letterhead

Tavi, we need a letterhead/banner for our blog, which is titled "Lantern Horizons". The letterhead/banner should incorporate the enclosed banner image, logo, and the name of our blog ("Lantern Horizons").

We would also like an alternative design that includes our picture. Here, we have two options that we would like to see.

In all, we would like to see 3 different designs: one banner without any pics; and two banner with two versions of our pictures.

The file size should be able to be resized for the space given to us at our website (http://bramblecrest-capital-partners.com).

We also need the letterhead/banner by Friday, June 13. Thanks!!

```html
<!DOCTYPE html>
<html lang="en">
<head>
<meta charset="utf-8">
<title>Lantern Horizons – Blog Banner</title>
<link rel="stylesheet" href="https://fonts.googleapis.com/css2?family=Arimo:ital,wght@0,400;1,400&display=swap">
<style>
  :root {
    --banner-bg: #000000;
    --title-gold: #c9b765;
    --rule-grey: #b4b4b4;
    --badge-bg: #1b1918;
    --badge-text: #ece7c9;
  }
  html, body {
    margin: 0;
    padding: 0;
    width: 1200px;
    height: 250px;
    overflow: hidden;
    background: var(--banner-bg);
  }
  .banner {
    position: relative;
    width: 1200px;
    height: 250px;
    background: var(--banner-bg);
    font-family: "Arimo", Arial, sans-serif;
  }
  .blog-title {
    margin: 0;
    font-weight: 400;
    font-style: italic;
    color: var(--title-gold);
    font-size: 88px;
    line-height: 1;
  }
  .blog-title span {
    position: absolute;
    white-space: nowrap;
  }
  .title-first { left: 34px; top: 30px; }
  .title-second { left: 230px; top: 124px; }
  .rules {
    position: absolute;
    left: 0;
    top: 0;
  }
  .rule { stroke: var(--rule-grey); stroke-width: 3; }
  .company-badge {
    position: absolute;
    left: 875px;
    top: 25px;
    width: 297px;
    height: 200px;
    background: var(--badge-bg);
    display: flex;
    align-items: flex-end;
    justify-content: center;
    box-sizing: border-box;
    padding: 0 16px 28px;
  }
  .company-name {
    margin: 0;
    color: var(--badge-text);
    font-family: "Arimo", Arial, sans-serif;
    font-weight: 400;
    font-size: 24px;
    line-height: 1.2;
    text-align: center;
  }
</style>
</head>
<body>
  <header class="banner">
    <h1 class="blog-title">
      <span class="title-first">Lantern</span>
      <span class="title-second">Horizons</span>
    </h1>

    <svg class="rules" width="1200" height="250" viewBox="0 0 1200 250" aria-hidden="true">
      <line class="rule" x1="497" y1="66" x2="819" y2="66"/>
      <line class="rule" x1="497" y1="92" x2="819" y2="92"/>
      <line class="rule" x1="35" y1="155" x2="200" y2="155"/>
      <line class="rule" x1="35" y1="176" x2="200" y2="176"/>
    </svg>

    <div class="company-badge">
      <p class="company-name">Bramblecrest<br>Capital Partners</p>
    </div>
  </header>
</body>
</html>
```